Flyer / Mailer for Business Debt Relief Business - Tillbrook Partners 6" x 11"

We need a 6" x 11" double sided flyer. This will be sent out to potential customers with high interest business loans. We would like the design to coordinate with the colors of our logo. I have included a mock up that we sketched out. I have also included a file of a mailer we received that we would like to use as a template (not colors or fonts, just set up). I have also included an .ai file of our logo.

```html
<!DOCTYPE html>
<html lang="en">
<head>
<meta charset="utf-8">
<title>Tillbrook Partners – Mailer</title>
<link href="https://fonts.googleapis.com/css2?family=Lato:ital,wght@0,300;0,400;0,700;0,900;1,400;1,700&display=swap" rel="stylesheet">
<style>
  :root {
    --navy: #1f5a9c;
    --blue: #0a86bf;
    --blue-deep: #0b5f8e;
    --green: #76b843;
    --green-dark: #4f8f2a;
    --mist: #eceef3;
    --ink: #3a3a3a;
    --white: #ffffff;
  }
  * { box-sizing: border-box; margin: 0; padding: 0; }
  html, body { width: 1200px; height: 1200px; overflow: hidden; background: var(--white); }
  body { position: relative; font-family: "Lato", sans-serif; color: var(--ink); }

  .card { position: absolute; left: 60px; width: 1082px; overflow: hidden; background: var(--white); }
  .card--front { top: 40px; height: 558px; }
  .card--back { top: 621px; height: 537px; border: 1px solid #e4e4e4; }

  /* photo column */
  .photo-column { position: absolute; left: 0; top: 0; width: 226px; height: 558px; background: var(--white); }
  .photo { position: absolute; left: 0; width: 226px; }
  .photo--cash { top: 0; height: 136px; background: linear-gradient(135deg, #6d7a6a, #c9cfc4 55%, #8a8f86); }
  .photo--desk { top: 138px; height: 283px; background: linear-gradient(160deg, #3c4046, #24272b 55%, #9c9a94); }
  .photo--coins { top: 423px; height: 135px; background: linear-gradient(180deg, #b9c46a, #8fa54a 55%, #a0835b); }

  .panel { position: absolute; left: 226px; right: 0; }
  .panel--header { top: 0; height: 88px; background: var(--mist); }
  .headline { position: absolute; left: 24px; top: 50px; font-weight: 900; font-size: 26px; color: var(--navy); letter-spacing: -0.2px; }
  .brand-mini { position: absolute; right: 58px; top: 36px; display: flex; align-items: center; gap: 6px; font-size: 12px; font-weight: 700; color: var(--navy); letter-spacing: 0.5px; }
  .brand-mini .mark { width: 14px; height: 14px; background: var(--green); }

  .panel--intro { top: 88px; height: 66px; background: var(--green); color: var(--white); text-align: center; font-style: italic; font-size: 22px; letter-spacing: 2.6px; line-height: 27px; padding-top: 6px; }

  .panel--offer { top: 154px; height: 242px; background: var(--blue); }
  .photo--advisor { position: absolute; right: 0; top: 0; width: 330px; height: 242px; background: linear-gradient(90deg, var(--blue) 0%, #2f6f95 30%, #3b4752 65%, #6a6f74 100%); }
  .offer-title { position: absolute; left: 30px; top: 6px; color: var(--white); font-weight: 900; font-size: 27px; line-height: 33px; }
  .benefits { position: absolute; left: 32px; top: 88px; list-style: none; color: var(--white); font-size: 12.5px; line-height: 17.3px; }
  .benefits li { position: relative; padding-left: 20px; }
  .benefits li::before { content: ""; position: absolute; left: 0; top: 5px; width: 9px; height: 7px; border-radius: 50%; background: var(--white); }

  .panel--contact { top: 396px; height: 162px; background: var(--green); color: var(--white); text-align: center; }
  .contact-line { font-style: italic; font-weight: 700; font-size: 22px; letter-spacing: 2.4px; line-height: 31px; }
  .contact-line:first-child { margin-top: 16px; }
  .phone { font-weight: 700; font-size: 40px; letter-spacing: 4px; line-height: 46px; }
  .email { font-style: italic; font-weight: 700; font-size: 16px; margin-top: 4px; }

  /* back */
  .return-block { position: absolute; left: 52px; top: 44px; width: 300px; text-align: center; }
  .brand { display: flex; align-items: center; justify-content: center; gap: 10px; margin-top: 68px; font-size: 22px; font-weight: 400; letter-spacing: 2px; color: var(--ink); }
  .brand .mark { width: 18px; height: 18px; background: var(--green); }
  .address { margin-top: 18px; font-weight: 300; font-size: 13.5px; line-height: 16px; color: var(--ink); }
  .back-title { position: absolute; left: 50px; top: 225px; font-weight: 900; font-size: 22px; line-height: 26px; color: var(--ink); }
  .back-copy { position: absolute; left: 50px; top: 301px; font-style: italic; font-size: 19.5px; line-height: 23px; color: var(--ink); }
  .stamp-box { position: absolute; left: 901px; top: 43px; width: 118px; height: 126px; border: 1px solid #555; }
</style>
</head>
<body>
  <section class="card card--front">
    <div class="photo-column">
      <div class="photo photo--cash" role="img" aria-label="Photo of a hand holding dollar bills"></div>
      <div class="photo photo--desk" role="img" aria-label="Photo of a person counting cash at a desk with a calculator and ledger"></div>
      <div class="photo photo--coins" role="img" aria-label="Photo of coin stacks with seedlings growing on top"></div>
    </div>

    <div class="panel panel--header">
      <h1 class="headline">HELPING BUSINESSES FOCUS ON WHAT METTERS!</h1>
      <div class="brand-mini"><span class="mark"></span>TILLBROOK PARTNERS</div>
    </div>

    <div class="panel panel--intro">
      <p>We understand that merchant cash advance<br>loans can be a burden on your business</p>
    </div>

    <div class="panel panel--offer">
      <div class="photo--advisor" role="img" aria-label="Photo of a businessman in a suit reviewing a tablet at a laptop"></div>
      <h2 class="offer-title">Over whelmed by daily/weekly payments?<br>WE CAN HELP!</h2>
      <ul class="benefits">
        <li>This is not a loan, WE ARE NOT LENDERS!</li>
        <li>Improve your business cash flow immediately</li>
        <li>Move payments to one monthly amount</li>
        <li>Reduce the amount you are paying out monthly</li>
        <li>Strategic alternatives to high interest loans</li>
        <li>Fast, confidential business debt relief</li>
        <li>No obligation consultation</li>
        <li>Absolutely no credit pulls</li>
        <li>No collateral, no financia’s</li>
      </ul>
    </div>

    <div class="panel panel--contact">
      <p class="contact-line">Visit our website:&nbsp; www.tillbrookpartners.com</p>
      <p class="contact-line">Call NOW for free consultation with our experts</p>
      <p class="phone">844-555-0199</p>
      <p class="email">email: info@tillbrookpartners.com</p>
    </div>
  </section>

  <section class="card card--back">
    <div class="return-block">
      <div class="brand"><span class="mark"></span>Tillbrook Partners</div>
      <p class="address">1450 W Harlow Ave<br>Brenton, Calder County 76010</p>
    </div>
    <h2 class="back-title">Strategic Debt Relief For<br>Businesses of All Sizies</h2>
    <p class="back-copy">Stop taking out loans to pay off<br>other loans.<br>Take back your business’s cash<br>flow, and focus on what matters.</p>
    <div class="stamp-box"></div>
  </section>
</body>
</html>
```